Brantley Metal Roofing INC.

Hello,
I am working with a local business to design them a new website. The designer I had worked with moved to colorado and has taken a new job. He recommended that I try posting my new jobs on here. I would need a design and assistance setting the site up on my hostmerry server. I work by myself and handle the sales side of things and need a designer that can help me out.
This company is a metal roofing business. The current page I made for them is www.brantleymetalinc.example

They would like the new site to be similar to http://www.dovecreekalloy.example

Please let me know if this is something that you could do for us.
Updates

the company wants the site to look very similar to this http://www.dovecreekalloy.exampleis that something you could do, please get in touch with me.Thanks Added Tuesday, January 10, 2017

Industry/Entity Type

Business

Font styles to use
Sans Serif

Colors
ed252d

Requirements
Must have
• the company wants the site to look very similar to this
• http://www.dovecreekalloy.example
• is that something you could do, please get in touch with me.
• Thanks

```html
<!DOCTYPE html>
<html lang="en">
<head>
<meta charset="utf-8">
<title>Brantley Metal Inc</title>
<link href="https://fonts.googleapis.com/css2?family=Zilla+Slab:wght@400;500;600&family=Montserrat:wght@500&display=swap" rel="stylesheet">
<style>
:root{
  --red:#ed252d;
  --dark:#3b3b3b;
  --footer:#5b5b5b;
  --footer-bottom:#4b4b4b;
  --cream:#f4efe8;
  --text:#222;
  --muted:#666;
  --line:#d8d8d8;
}
*{margin:0;padding:0;box-sizing:border-box}
html,body{width:738px;height:1200px;overflow:hidden;background:#fff}
body{position:relative;font-family:"Zilla Slab",Georgia,serif;color:var(--text)}
.abs{position:absolute}
.topbar{left:0;top:0;width:738px;height:26px;background:var(--dark);color:#fff}
.topbar .phone{left:100px;top:6px;font-size:9px;display:flex;align-items:center;gap:6px}
.topbar .phone .ico{width:12px;height:12px;border:1px solid #fff;display:flex;align-items:center;justify-content:center}
.topbar .promo{left:288px;top:4px;font-size:13px;font-weight:500;display:flex;align-items:center;gap:8px}
.topbar .promo .dot{width:10px;height:12px;background:var(--red);border-radius:2px}
.search{left:539px;top:4px;width:99px;height:18px;border:1px solid #888;background:#2e2e2e;font-size:6px;color:#aaa;padding:5px 9px}
.search .btn{position:absolute;right:-1px;top:-1px;width:19px;height:18px;background:var(--red);display:flex;align-items:center;justify-content:center}
.brand{left:98px;top:40px;width:130px;text-align:center}
.brand .mark{width:12px;height:12px;background:var(--red);margin:0 auto 12px}
.brand .name{font-family:Montserrat,Arial,sans-serif;font-weight:500;font-size:11px;color:var(--red);letter-spacing:.3px;white-space:nowrap}
.nav{top:54px;font-size:8.5px;font-weight:500;display:flex;gap:0}
.nav a{position:absolute;color:var(--text);text-decoration:none;white-space:nowrap}
.nav a.active{color:var(--red)}
.quote{left:575px;top:49px;width:64px;height:17px;background:var(--red);color:#fff;font-size:9px;text-align:center;line-height:17px}
.hero{left:99px;top:92px;width:540px;height:252px;background:linear-gradient(180deg,#a9b3b8 0%,#7d8b80 35%,#6e5e52 65%,#4f5a3d 100%)}
.hero .arrow{position:absolute;top:114px;width:24px;height:26px;background:rgba(255,255,255,.55);display:flex;align-items:center;justify-content:center}
.hero .caption{position:absolute;left:113px;top:172px;width:322px;height:52px;background:rgba(60,60,60,.55);color:#fff;font-size:12.5px;font-weight:600;text-align:center;line-height:18px;padding-top:7px}
.feature{top:352px;width:176px;height:88px;border:1px solid var(--line);text-align:center;font-size:9.5px;font-weight:500;line-height:12px}
.feature svg{display:block;margin:16px auto 9px}
.feature.hl{color:var(--red)}
.products{left:0;top:462px;width:738px;height:300px;background:var(--cream)}
.tag{height:30px;background:var(--red);color:#fff;font-size:12.5px;font-weight:500;text-align:center;line-height:30px}
.card{top:542px;width:130px;height:188px;background:#fff;border:1px solid var(--line);padding:0 18px}
.card .sheet{height:66px;margin:18px 4px 16px;border-radius:2px}
.card h3{font-size:9.5px;font-weight:500;margin-bottom:6px}
.card p{font-size:6.3px;color:var(--muted);line-height:10px}
.card .more{font-size:6px;color:var(--red);margin-top:8px}
.chev{width:14px;height:24px}
.proj{top:846px;width:133px;height:131px}
.proj span{position:absolute;left:0;right:0;top:58px;text-align:center;color:#fff;font-size:9px}
.footer{left:0;top:1022px;width:738px;height:140px;background:var(--footer);color:#fff}
.footer h4{position:absolute;top:32px;font-size:12.5px;font-weight:500}
.footer .col{position:absolute;top:56px;font-size:6.3px;line-height:13.7px}
.footer .row{display:flex;align-items:center;gap:5px}
.social{display:flex;gap:5px}
.social i{width:13px;height:13px;border-radius:50%;background:#fff;display:block}
.bottom{left:0;top:1162px;width:738px;height:38px;background:var(--footer-bottom);color:#fff;font-size:6.5px}
</style>
</head>
<body>

<div class="abs topbar">
  <div class="abs phone"><span class="ico"><svg width="7" height="7" viewBox="0 0 10 10"><path d="M2 1l2 2-1 1.2c.6 1.3 1.5 2.2 2.8 2.8L7 6l2 2-1.3 1.3C4.5 9 1 5.5.7 2.3z" fill="#fff"/></svg></span>555-014-0276</div>
  <div class="abs promo"><span class="dot"></span>Customize Your Project <span style="margin-left:6px">&gt;</span></div>
  <div class="abs search">Search<span class="btn"><svg width="9" height="9" viewBox="0 0 10 10"><circle cx="4" cy="4" r="3" fill="none" stroke="#fff" stroke-width="1.3"/><path d="M6.3 6.3L9 9" stroke="#fff" stroke-width="1.3"/></svg></span></div>
</div>

<div class="abs brand"><div class="mark"></div><div class="name">BRANTLEY METAL INC</div></div>

<nav class="abs nav" style="left:0;width:738px">
  <a class="active" style="left:301px">Home</a>
  <a style="left:340px">About Us</a>
  <a style="left:390px">Products</a>
  <a style="left:441px">Blog</a>
  <a style="left:474px">Project</a>
  <a style="left:517px">Contact Us</a>
</nav>
<div class="abs quote">Get a Quote</div>

<section class="abs hero" role="img" aria-label="Photo of a house with a silver standing-seam metal roof among trees">
  <div class="arrow" style="left:0;border-radius:0 13px 13px 0"><svg width="7" height="12" viewBox="0 0 7 12"><path d="M6 1L1 6l5 5" fill="none" stroke="#444"/></svg></div>
  <div class="arrow" style="right:0;border-radius:13px 0 0 13px"><svg width="7" height="12" viewBox="0 0 7 12"><path d="M1 1l5 5-5 5" fill="none" stroke="#444"/></svg></div>
  <div class="caption">Lorem ipsum dolor sit amet, consectetuer<br>adipiscing elit. Aenean commodo ligula eget dolor.</div>
</section>

<div class="abs feature" style="left:99px">
  <svg width="26" height="26" viewBox="0 0 26 26" fill="none" stroke="#111" stroke-width="2.4"><path d="M6 1v19h19"/><path d="M1 6h19v19"/><path d="M3 23L23 3"/></svg>
  Complete Post Frame<br>Building Packages
</div>
<div class="abs feature hl" style="left:281px">
  <svg width="26" height="26" viewBox="0 0 26 26" fill="none" stroke="#ed252d" stroke-width="1.6"><path d="M2 12L13 2l11 10"/><path d="M5 10v14h16V10"/><rect x="8" y="14" width="5" height="10"/><rect x="15" y="14" width="4" height="4"/><path d="M18 4v4"/></svg>
  Residental<br>Metal Roofing
</div>
<div class="abs feature" style="left:462px">
  <svg width="26" height="26" viewBox="0 0 26 26" fill="none" stroke="#111" stroke-width="1.6"><rect x="8" y="2" width="10" height="22"/><rect x="2" y="10" width="6" height="14"/><rect x="18" y="8" width="6" height="16"/><path d="M11 6h1M14 6h1M11 10h1M14 10h1M11 14h1M14 14h1M11 18h1M14 18h1M4 14h2M4 18h2M20 12h2M20 16h2M20 20h2"/></svg>
  Commercial &amp;<br>Agricultural Applications
</div>

<section class="abs products">
  <div class="abs tag" style="left:319px;top:28px;width:98px">Our Products</div>
</section>
<svg class="abs chev" style="left:78px;top:624px" viewBox="0 0 14 24"><path d="M12 1L2 12l10 11" fill="none" stroke="#ed252d" stroke-width="1.2"/></svg>
<svg class="abs chev" style="left:646px;top:624px" viewBox="0 0 14 24"><path d="M2 1l10 11L2 23" fill="none" stroke="#ed252d" stroke-width="1.2"/></svg>

<article class="abs card" style="left:99px"><div class="sheet" role="img" aria-label="Red corrugated metal roofing sheet" style="background:linear-gradient(90deg,#b8141a,#ef3a3f,#b8141a,#ef3a3f,#b8141a)"></div><h3>Sample Text Here</h3><p>Lorem ipsum dolor sit amet,<br>consectetuer adipiscing elit.<br>Lorem ipsum dolor</p><div class="more">Read More &gt;</div></article>
<article class="abs card" style="left:236px"><div class="sheet" role="img" aria-label="Turquoise corrugated metal roofing sheet" style="background:linear-gradient(90deg,#0f8fa0,#38c6d6,#0f8fa0,#38c6d6,#0f8fa0)"></div><h3>Sample Text Here</h3><p>Lorem ipsum dolor sit amet,<br>consectetuer adipiscing elit.<br>Lorem ipsum dolor</p><div class="more">Read More &gt;</div></article>
<article class="abs card" style="left:373px"><div class="sheet" role="img" aria-label="Yellow corrugated metal roofing sheet" style="background:linear-gradient(90deg,#c98f05,#f5c025,#c98f05,#f5c025,#c98f05)"></div><h3>Sample Text Here</h3><p>Lorem ipsum dolor sit amet,<br>consectetuer adipiscing elit.<br>Lorem ipsum dolor</p><div class="more">Read More &gt;</div></article>
<article class="abs card" style="left:509px"><div class="sheet" role="img" aria-label="Pale teal corrugated metal roofing sheet" style="background:linear-gradient(90deg,#6fb7b3,#a6dcd8,#6fb7b3,#a6dcd8,#6fb7b3)"></div><h3>Sample Text Here</h3><p>Lorem ipsum dolor sit amet,<br>consectetuer adipiscing elit.<br>Lorem ipsum dolor</p><div class="more">Read More &gt;</div></article>

<div class="abs tag" style="left:322px;top:792px;width:109px">Recent Projects</div>
<svg class="abs chev" style="left:78px;top:899px" viewBox="0 0 14 24"><path d="M12 1L2 12l10 11" fill="none" stroke="#ed252d" stroke-width="1.2"/></svg>
<svg class="abs chev" style="left:646px;top:899px" viewBox="0 0 14 24"><path d="M2 1l10 11L2 23" fill="none" stroke="#ed252d" stroke-width="1.2"/></svg>

<div class="abs proj" style="left:100px;background:linear-gradient(160deg,#5a1a1a,#3a1010)" role="img" aria-label="Close-up of dark red metal roof tiles"></div>
<div class="abs proj" style="left:235px;background:linear-gradient(160deg,#4d525b,#6b4a44)" role="img" aria-label="Worker spraying a coating on a copper roof"></div>
<div class="abs proj" style="left:370px;background:linear-gradient(160deg,#2f333a,#3f4248)" role="img" aria-label="Gable of a house with a dark shingle roof"><span>Sample Text Here</span></div>
<div class="abs proj" style="left:505px;background:linear-gradient(160deg,#a5aeb6,#9a4a46)" role="img" aria-label="Roofers installing red metal tile roofing"></div>

<footer class="abs footer">
  <h4 style="left:99px">About Us</h4>
  <div class="col" style="left:99px;width:150px">Lorem ipsum dolor sit amet, consectetuer adipiscing elit. Aenean commodo ligula eget dolor. Aenean massa. Cum sociis natoque penatibus et magnis dis parturient montes, nascetur ridiculus mus.</div>
  <h4 style="left:297px">Address</h4>
  <div class="col" style="left:295px">
    <div class="row"><svg width="6" height="8" viewBox="0 0 6 8"><path d="M3 8C1 5 0 4 0 3a3 3 0 016 0c0 1-1 2-3 5z" fill="#fff"/></svg>66 Lorem ipsum dolor sit amet .</div>
    <div class="row"><svg width="6" height="6" viewBox="0 0 10 10"><path d="M2 1l2 2-1 1.2c.6 1.3 1.5 2.2 2.8 2.8L7 6l2 2-1.3 1.3C4.5 9 1 5.5.7 2.3z" fill="#fff"/></svg>555-014-0276</div>
    <div class="row"><svg width="7" height="5" viewBox="0 0 7 5"><rect width="7" height="5" fill="#fff"/><path d="M0 0l3.5 3L7 0" fill="none" stroke="#5b5b5b" stroke-width=".7"/></svg>info@company.com</div>
  </div>
  <h4 style="left:446px">Quick Links</h4>
  <div class="col" style="left:446px">::&nbsp; About Us<br>::&nbsp; Services<br>::&nbsp; Products<br>::&nbsp; Blog<br>::&nbsp; Contact Us</div>
  <h4 style="left:575px">Follow us</h4>
  <div class="col social" style="left:577px;top:52px"><i></i><i></i><i></i></div>
</footer>
<div class="abs bottom"><span class="abs" style="left:100px;top:15px">Copyright © 2017 BRANTLEY METAL INC - All Rights Reserved.</span></div>

</body>
</html>
```